Solar accessories banner to produce more green energy

Hello,
we need a banner for a solar accessories page.
https://plovinta.de/index.php/zubehoer/
as we are commissioning the first banner for the entire homepage here, we are open to all directions. The current existing banner is just a random image of the installed theme and should not be a reference.
The banner should be created in a dark style. Our core colors are black / yellow / white.
The banner should have a clear reference to the accessories shown below and consider other accessories such as mounting systems of solar panels, cables, adapters, etc.
I would be happy to answer any queries.
Regards
Malte
-------------------------------------------------- ----------------------------------------------
Hello,
https://plovinta.de/index. php / accessories /
Since we are commissioning the first banner for the entire homepage, we are open to all directions. The currently existing banner is only a random image of the installed theme and is not intended to be a reference.
The banner should be created in a dark stem. Our core colors are black / yellow / white.
The banner should have a clear reference to the accessories shown below and take into account other accessories such as mounting systems for solar panels, cables, adapters, etc.
I am happy to answer any questions.
greetings
Malte

```html
<!DOCTYPE html>
<html lang="de">
<head>
<meta charset="utf-8">
<title>Montage und Anschluss – Zubehör</title>
<link href="https://fonts.googleapis.com/css2?family=Nunito:wght@400;700;800;900&display=swap" rel="stylesheet">
<style>
  :root {
    --bg: #161616;
    --bg-shape: #262626;
    --yellow: #ffcc00;
    --white: #ffffff;
    --ink: #151515;
    --muted: #b9b9b9;
  }
  * { margin: 0; padding: 0; box-sizing: border-box; }
  html, body { width: 1200px; height: 439px; overflow: hidden; background: var(--bg); }
  .banner {
    position: relative;
    width: 1200px;
    height: 439px;
    overflow: hidden;
    background: var(--bg);
    font-family: "Nunito", sans-serif;
  }
  .decor { position: absolute; inset: 0; width: 1200px; height: 439px; }
  .content { position: absolute; left: 82px; top: 94px; width: 520px; }
  .headline {
    color: var(--white);
    font-weight: 900;
    font-size: 50px;
    line-height: 53px;
    letter-spacing: 0.3px;
    text-transform: uppercase;
    white-space: nowrap;
  }
  .headline .accent {
    background: var(--yellow);
    color: var(--ink);
    padding: 0 3px;
  }
  .intro {
    margin-top: 18px;
    color: var(--muted);
    font-size: 12px;
    line-height: 21.5px;
    width: 410px;
  }
  .video-button {
    position: absolute;
    left: 0;
    top: 210px;
    width: 373px;
    height: 49px;
    border-radius: 25px;
    background: var(--yellow);
    color: var(--ink);
    display: flex;
    align-items: center;
    padding-left: 21px;
    font-weight: 800;
    font-size: 12px;
    letter-spacing: 0.1px;
    text-decoration: none;
    text-transform: uppercase;
  }
  .video-button svg { margin-right: 12px; }
  .product-photo {
    position: absolute;
    left: 520px;
    top: 15px;
    width: 670px;
    height: 320px;
    background: radial-gradient(ellipse 50% 50% at 50% 50%, rgba(28,28,28,0.95) 0%, rgba(34,34,34,0.75) 45%, rgba(40,40,40,0) 100%);
  }
</style>
</head>
<body>
  <section class="banner">
    <svg class="decor" viewBox="0 0 1200 439" aria-hidden="true">
      <rect class="corner-shape" x="-60" y="-120" width="160" height="160" rx="26" fill="var(--bg-shape)" transform="rotate(45 20 -40)"/>
      <rect class="feature-diamond" x="636" y="-123" width="440" height="440" rx="48" fill="var(--white)" transform="rotate(45 856 97)"/>
      <rect class="accent-diamond" x="1148" y="302" width="160" height="160" rx="34" fill="var(--yellow)" transform="rotate(45 1228 382)"/>
    </svg>

    <div class="product-photo" role="img" aria-label="Photo of black solar Y-branch and triple-branch cable connectors"></div>

    <div class="content">
      <h1 class="headline">Montage <span class="accent">und</span><br>Anschluss</h1>
      <p class="intro">Unser Zubehörsortiment ist auf die angebotenen Produkte perfekt abgestimmt. So finden Sie zu allen Bereichen passende Stecker, Kabel, Adapter, Halterungen, uvm.</p>
      <a class="video-button" href="#">
        <svg width="14" height="14" viewBox="0 0 14 14" aria-hidden="true">
          <circle cx="7" cy="7" r="7" fill="var(--ink)"/>
          <path d="M5.5 4.3 L9.8 7 L5.5 9.7 Z" fill="var(--yellow)"/>
        </svg>
        Videovorstellung der einzelnen Produkte
      </a>
    </div>
  </section>
</body>
</html>
```